Attract renters to our neighborhoods - inform renters who we are

Apartments in several neighborhoods. We want to attract renters who want to live along the lake or other near by neighborhoods. We want them to know that we have an apartment for them in their location.
The perfect location to spend your time.
When minutes matter LIVE where you work and play! (love this tag line)
Updates

www.qrvlofthomes.example Choose from over 3,700 apartments in Chicago’s most celebrated neighborhoods. 555-218-6043 Chicago’s most celebrated neighborhoods. 31 PROPERTIES

Target Market(s)

Sophisticated apartment renter who wants location, space, amenities

Industry/Entity Type

Apartment Rentals

Requirements
Must have
• Feel like I want to live there, or the ad is calling me
Nice to have
• Appeal to a sophisticated apartment renter. We have what you want, where you want to be.
Should not have
• Logo colors are black and red/burnt orange see attached logo

```html
<!DOCTYPE html>
<html lang="en">
<head>
<meta charset="utf-8">
<title>QRV Apartments – Banner Set</title>
<link href="https://fonts.googleapis.com/css2?family=Open+Sans:ital,wght@0,400;0,600;0,700;0,800;1,700;1,800&family=Saira+Semi+Condensed:wght@400;500&display=swap" rel="stylesheet">
<style>
  :root {
    --brand-red: #8c171c;
    --brand-red-dark: #5a0b0f;
    --cta-red: #ee1d1d;
    --panel-dark: rgba(28, 8, 9, 0.9);
    --ink: #0b0b0b;
    --paper: #fdf0f0;
    --tag-yellow: #f4e71d;
    --ring-yellow: #f2c21b;
    --ring-grey: #b9b4b4;
    --glow: rgba(226, 150, 158, 0.55);
    --white: #ffffff;
    --photo: linear-gradient(180deg, #8fd1e3 0%, #c9e6ec 30%, #d9b9a0 46%, #b0664a 54%, #34502b 64%, #5d7a3a 70%, #c08668 78%, #7f5b4d 86%, #a9cdd6 100%);
  }
  * { box-sizing: border-box; margin: 0; padding: 0; }
  html, body { width: 1200px; height: 960px; overflow: hidden; }
  body {
    background: var(--white);
    font-family: "Open Sans", Arial, sans-serif;
    position: relative;
  }
  .backdrop {
    position: absolute; left: 20px; top: 45px; width: 1160px; height: 870px;
    background: #f2cdd0;
    box-shadow: 0 0 50px 30px var(--glow);
    border-radius: 20px;
  }
  .banner { position: absolute; overflow: hidden; }
  .photo { position: absolute; background: var(--photo); }
  .brand-mark {
    position: absolute; background: var(--white);
    display: flex; align-items: center; justify-content: center; gap: 5px;
    font-weight: 800; color: var(--ink); letter-spacing: -1px;
  }
  .brand-mark .dot { background: var(--cta-red); display: block; }
  .cta {
    position: absolute; background: var(--cta-red); color: var(--white);
    font-weight: 700; letter-spacing: -0.3px; white-space: nowrap;
    display: flex; align-items: center; justify-content: space-between;
  }
  .cta svg { flex: none; }
  .intro { color: var(--white); font-weight: 400; letter-spacing: -0.4px; white-space: nowrap; }
  .headline { color: var(--white); font-weight: 800; letter-spacing: -0.6px; white-space: nowrap; }
  .tagline { font-family: "Saira Semi Condensed", "Arial Narrow", sans-serif; color: var(--tag-yellow); font-weight: 400; white-space: nowrap; }
  .phone { color: var(--white); font-weight: 800; font-style: italic; white-space: nowrap; }
  .web { color: var(--white); font-weight: 600; white-space: nowrap; }
  .stripes { position: absolute; }

  /* Square dark-panel banner */
  .sq-dark { left: 35px; top: 65px; width: 546px; height: 546px; background: var(--brand-red); }
  .sq-dark .photo { left: 185px; top: 0; width: 361px; height: 546px; }
  .sq-dark .brand-mark { left: 81px; top: 32px; width: 104px; height: 63px; font-size: 36px; }
  .sq-dark .brand-mark .dot { width: 9px; height: 9px; }
  .sq-dark .panel { position: absolute; left: 81px; top: 95px; width: 289px; height: 357px; background: var(--panel-dark); }
  .sq-dark .intro { position: absolute; left: 29px; top: 25px; font-size: 20px; line-height: 21px; }
  .sq-dark .headline { position: absolute; left: 29px; top: 89px; font-size: 32px; line-height: 38px; }
  .sq-dark .rule { position: absolute; left: 29px; top: 222px; width: 208px; height: 1px; background: rgba(255,255,255,.7); }
  .sq-dark .tagline { position: absolute; left: 29px; top: 234px; font-size: 18px; line-height: 25px; }
  .sq-dark .cta { left: 110px; top: 392px; width: 191px; height: 38px; font-size: 11.5px; padding: 0 12px; }
  .sq-dark .contact { position: absolute; right: 373px; top: 478px; text-align: right; }
  .sq-dark .phone { font-size: 14px; line-height: 18px; }
  .sq-dark .web { font-size: 12px; line-height: 18px; margin-top: 2px; }
  .sq-dark .stripes { left: 60px; top: 160px; }

  /* Wide dark-panel banner */
  .wide-dark { left: 614px; top: 67px; width: 546px; height: 248px; background: var(--brand-red); }
  .wide-dark .photo { left: 199px; top: 0; width: 347px; height: 248px; }
  .wide-dark .brand-mark { left: 0; top: 15px; width: 68px; height: 40px; font-size: 23px; gap: 3px; }
  .wide-dark .brand-mark .dot { width: 6px; height: 6px; }
  .wide-dark .side-contact {
    position: absolute; left: 18px; bottom: 20px;
    writing-mode: vertical-rl; transform: rotate(180deg);
    display: flex; gap: 5px; white-space: nowrap;
  }
  .wide-dark .phone { font-size: 12px; line-height: 15px; }
  .wide-dark .web { font-size: 10.5px; line-height: 15px; font-weight: 400; }
  .wide-dark .panel { position: absolute; left: 68px; top: 14px; width: 221px; height: 234px; background: var(--panel-dark); }
  .wide-dark .intro { position: absolute; left: 21px; top: 21px; font-size: 14px; line-height: 15px; }
  .wide-dark .headline { position: absolute; left: 21px; top: 66px; font-size: 21px; line-height: 26px; }
  .wide-dark .rule { position: absolute; left: 23px; top: 162px; width: 160px; height: 1px; background: rgba(255,255,255,.7); }
  .wide-dark .tagline { position: absolute; left: 23px; top: 171px; font-size: 14px; line-height: 22px; }
  .wide-dark .cta { left: 358px; top: 194px; width: 188px; height: 39px; font-size: 11.5px; padding: 0 10px 0 12px; }

  /* Circle banners */
  .circle-photo { position: absolute; border-radius: 50%; background: var(--photo); }
  .rings { position: absolute; left: 0; top: 0; }
  .orb {
    position: absolute; border-radius: 50%; background: var(--ink);
    display: flex; flex-direction: column; align-items: center; justify-content: center; text-align: center;
  }
  .orb .intro { line-height: 1.12; }
  .circle-tag { position: absolute; text-align: center; color: var(--ink); font-weight: 400; white-space: nowrap; }

  .wide-circle { left: 35px; top: 648px; width: 546px; height: 248px; background: var(--paper); }
  .wide-circle .side { position: absolute; left: 0; top: 0; width: 171px; height: 248px; background: var(--brand-red); }
  .wide-circle .side-top { position: absolute; left: 0; top: 0; width: 171px; height: 54px; background: var(--brand-red-dark); }
  .wide-circle .phone { position: absolute; left: 13px; top: 84px; font-size: 20px; }
  .wide-circle .web { position: absolute; left: 13px; top: 121px; font-size: 11.5px; font-weight: 400; }
  .wide-circle .cta { left: 26px; top: 167px; width: 132px; height: 39px; font-size: 11.5px; line-height: 13px; padding: 0 12px 0 17px; font-weight: 600; white-space: normal; }
  .wide-circle .brand-mark { left: 218px; top: 2px; width: 81px; height: 47px; font-size: 26px; }
  .wide-circle .brand-mark .dot { width: 7px; height: 7px; }
  .wide-circle .circle-photo { left: 299px; top: 11px; width: 256px; height: 256px; }
  .wide-circle .circle-tag { left: 345px; top: 44px; width: 150px; font-size: 13.5px; line-height: 17px; }
  .wide-circle .orb { left: 196px; top: 99px; width: 164px; height: 164px; padding-bottom: 18px; }
  .wide-circle .orb .intro { font-size: 11px; }
  .wide-circle .orb .headline { font-size: 17px; line-height: 21px; margin-top: 6px; }

  .sq-circle { left: 614px; top: 351px; width: 546px; height: 546px; background: var(--paper); }
  .sq-circle .brand-mark { left: 29px; top: 28px; width: 103px; height: 61px; font-size: 34px; }
  .sq-circle .brand-mark .dot { width: 9px; height: 9px; }
  .sq-circle .circle-photo { left: 139px; top: 1px; width: 398px; height: 398px; }
  .sq-circle .circle-tag { left: 188px; top: 46px; width: 300px; font-size: 14.5px; line-height: 21px; }
  .sq-circle .orb { left: 75px; top: 233px; width: 214px; height: 214px; padding-bottom: 30px; }
  .sq-circle .orb .intro { font-size: 14px; }
  .sq-circle .orb .headline { font-size: 22px; line-height: 27px; margin-top: 10px; }
  .sq-circle .band { position: absolute; left: 0; top: 443px; width: 546px; height: 103px; background: var(--brand-red); }
  .sq-circle .band-edge { position: absolute; left: 0; top: 443px; width: 42px; height: 103px; background: var(--brand-red-dark); }
  .sq-circle .phone { position: absolute; left: 76px; top: 462px; font-size: 21px; }
  .sq-circle .web { position: absolute; left: 76px; top: 491px; font-size: 16px; letter-spacing: 0.3px; }
  .sq-circle .cta { left: 335px; top: 474px; width: 185px; height: 38px; font-size: 11.5px; padding: 0 11px; }
  .sq-circle .stripes { left: 0; top: 163px; }
</style>
</head>
<body>
  <div class="backdrop"></div>

  <!-- Square banner with dark text panel -->
  <section class="banner sq-dark">
    <div class="photo" role="img" aria-label="Photo of the city skyline across a calm lake, with trees and the towers reflected in the water"></div>
    <svg class="stripes" width="50" height="250" viewBox="0 0 50 250" aria-hidden="true">
      <g stroke="#4a0a0d" stroke-width="5">
        <line x1="40" y1="10" x2="2" y2="100"/><line x1="40" y1="40" x2="2" y2="130"/>
        <line x1="40" y1="70" x2="2" y2="160"/><line x1="40" y1="100" x2="2" y2="190"/>
        <line x1="40" y1="130" x2="2" y2="220"/><line x1="40" y1="160" x2="2" y2="250"/>
      </g>
    </svg>
    <div class="brand-mark">QRV<span class="dot"></span></div>
    <div class="panel">
      <p class="intro">Choose from over 3,700<br>appartments in</p>
      <h2 class="headline">Chicago’s most<br>celebrated<br>neighboroods.</h2>
      <div class="rule"></div>
      <p class="tagline">When minutes matter,<br>LIVE where you work and play!</p>
    </div>
    <a class="cta">Find your new appartment
      <svg width="14" height="12" viewBox="0 0 14 12"><path d="M0 4h7V0l7 6-7 6V8H0z" fill="#fff"/></svg></a>
    <div class="contact">
      <p class="phone">555-218-6043</p>
      <p class="web">www.qrvlofthomes.example</p>
    </div>
  </section>

  <!-- Wide banner with dark text panel -->
  <section class="banner wide-dark">
    <div class="photo" role="img" aria-label="Photo of the city skyline across a calm lake, with trees and the towers reflected in the water"></div>
    <div class="brand-mark">QRV<span class="dot"></span></div>
    <div class="side-contact">
      <p class="phone">555-218-6043</p>
      <p class="web">www.qrvlofthomes.example</p>
    </div>
    <div class="panel">
      <p class="intro">Choose from over 3,700<br>appartments in</p>
      <h2 class="headline">Chicago’s most<br>celebrated<br>neighboroods.</h2>
      <div class="rule"></div>
      <p class="tagline">When minutes matter,<br>LIVE where you work and play!</p>
    </div>
    <a class="cta">Find your new appartment
      <svg width="14" height="12" viewBox="0 0 14 12"><path d="M0 4h7V0l7 6-7 6V8H0z" fill="#fff"/></svg></a>
  </section>

  <!-- Wide banner with circles -->
  <section class="banner wide-circle">
    <svg class="rings" width="546" height="248" viewBox="0 0 546 248" aria-hidden="true">
      <circle cx="430" cy="136" r="140" fill="none" stroke="var(--ring-grey)" stroke-width="1.2"/>
    </svg>
    <div class="circle-photo" role="img" aria-label="Round photo of the city skyline over a lake with its reflection"></div>
    <p class="circle-tag">When minutes<br>matter,&nbsp; LIVE where<br>you work and play!</p>
    <div class="side"></div>
    <div class="side-top"></div>
    <p class="phone">555-218-6043</p>
    <p class="web">www.qrvlofthomes.example</p>
    <a class="cta"><span>Find your new<br>appartment</span>
      <svg width="14" height="12" viewBox="0 0 14 12"><path d="M0 4h7V0l7 6-7 6V8H0z" fill="#fff"/></svg></a>
    <div class="brand-mark">QRV<span class="dot"></span></div>
    <svg class="rings" width="546" height="248" viewBox="0 0 546 248" aria-hidden="true">
      <circle cx="271" cy="169" r="97" fill="none" stroke="var(--cta-red)" stroke-width="1.8"/>
      <circle cx="285" cy="175" r="99" fill="none" stroke="var(--ring-yellow)" stroke-width="1.2"/>
    </svg>
    <div class="orb">
      <p class="intro">Choose from<br>over 3,700 appartments in</p>
      <h2 class="headline">Chicago’s most<br>celebrated<br>neighboroods.</h2>
    </div>
  </section>

  <!-- Square banner with circles -->
  <section class="banner sq-circle">
    <svg class="rings" width="546" height="546" viewBox="0 0 546 546" aria-hidden="true">
      <circle cx="349" cy="196" r="220" fill="none" stroke="var(--ring-grey)" stroke-width="1.3"/>
    </svg>
    <div class="circle-photo" role="img" aria-label="Round photo of the city skyline over a lake with its reflection"></div>
    <p class="circle-tag">When minutes matter,<br>LIVE where you work and play!</p>
    <div class="brand-mark">QRV<span class="dot"></span></div>
    <svg class="stripes" width="30" height="110" viewBox="0 0 30 110" aria-hidden="true">
      <g stroke="#5a5a5a" stroke-width="4">
        <line x1="28" y1="2" x2="0" y2="40"/><line x1="28" y1="20" x2="0" y2="58"/>
        <line x1="28" y1="38" x2="0" y2="76"/><line x1="28" y1="56" x2="0" y2="94"/>
        <line x1="28" y1="74" x2="0" y2="112"/>
      </g>
    </svg>
    <svg class="rings" width="546" height="546" viewBox="0 0 546 546" aria-hidden="true">
      <circle cx="171" cy="326" r="125" fill="none" stroke="var(--cta-red)" stroke-width="2"/>
      <circle cx="190" cy="329" r="127" fill="none" stroke="var(--ring-yellow)" stroke-width="1.3"/>
    </svg>
    <div class="orb">
      <p class="intro">Choose from<br>over 3,700 appartments in</p>
      <h2 class="headline">Chicago’s most<br>celebrated<br>neighboroods.</h2>
    </div>
    <div class="band"></div>
    <div class="band-edge"></div>
    <p class="phone">555-218-6043</p>
    <p class="web">www.qrvlofthomes.example</p>
    <a class="cta">Find your new appartment
      <svg width="14" height="12" viewBox="0 0 14 12"><path d="M0 4h7V0l7 6-7 6V8H0z" fill="#fff"/></svg></a>
  </section>
</body>
</html>
```